E-learning Information & Community Website Needs a Makeover

I'm looking for a design makeover for my website "Vetrola.club". Vetrola's aim is to connect people to online learning through forums, information, guides & independent reviews. The site was launched in September 2014 using a forum software (Xenforo), but now needs a more polished and sophisticated look which communicates expertise and professionalism. I would like to see designs that use the current "Vetrola" blue (#0070c0). To visit the current website, go to http://www.vetrola.club/

Target Market(s)

People wishing to study online

Industry/Entity Type

Club

Number of Pages Required

4 page

Font styles to use
Sans Serif

Requirements
Must have
• A simple, clear and sophisticated lading page with links to the site's key features: discussion forums, Useful resources, Reviews, News etc, Articles. (See layout idea file attached)
• The main pages are the Landing Page, Discussion Forums, Resources & Reviews
• I would like to see designs that use the current "Vetrola" blue (#0070c0).
Nice to have
• Something uncluttered and easy to understand. The design should convey expertise in the field of online learning, giving users a sense of trust in the site's offerings.
• To give an idea of the sort of thing I'm after, take a look at brantivo.com website (screenshot attached)

```html
<!DOCTYPE html>
<html lang="en">
<head>
<meta charset="utf-8">
<title>Vetrola – Connecting People to Online Learning</title>
<link href="https://fonts.googleapis.com/css2?family=Raleway:wght@400;500;600&family=Open+Sans:wght@400;600&display=swap" rel="stylesheet">
<style>
:root{
  --brand:#0070c0;
  --brand-dark:#005eaa;
  --brand-light:#1a8ad4;
  --ink:#333;
  --muted:#666;
  --tile-border:#d9d9d9;
  --band:#f1f1f1;
}
*{margin:0;padding:0;box-sizing:border-box}
html,body{width:796px;height:1200px;overflow:hidden;background:#fff}
body{position:relative;font-family:"Open Sans",Arial,sans-serif;color:var(--ink)}
.abs{position:absolute}

/* header */
.site-header{position:absolute;left:0;top:0;width:796px;height:66px;background:var(--brand)}
.brand-name{left:123px;top:14px;font-family:"Raleway",sans-serif;font-size:21px;font-weight:500;color:#fff}
.brand-tagline{left:123px;top:40px;font-size:8.5px;color:#fff}
.main-nav a{position:absolute;top:29px;font-family:"Raleway",sans-serif;font-size:10px;font-weight:500;color:#fff;text-decoration:none}
.btn-outline{position:absolute;top:24px;height:21px;border:1.5px solid #fff;border-radius:2px;color:#fff;font-family:"Raleway",sans-serif;font-size:8.5px;font-weight:600;display:flex;align-items:center;justify-content:center}

/* hero */
.hero{position:absolute;left:0;top:66px;width:796px;height:324px;background:radial-gradient(ellipse at 48% 40%,#e9e7e6 0%,#f2f2f3 45%,#f7f8f9 100%)}
.hero-title{position:absolute;left:0;width:796px;text-align:center;font-family:"Raleway",sans-serif;color:var(--brand)}
.hero-title.line1{top:109px;font-size:22.5px;font-weight:400}
.hero-title.line2{top:133px;font-size:29px;font-weight:400}
.hero-cta{position:absolute;left:343px;top:179px;width:112px;height:30px;background:var(--brand);color:#fff;font-family:"Raleway",sans-serif;font-weight:600;font-size:10.5px;display:flex;align-items:center;justify-content:center}
.hero-arrow{position:absolute;top:120px}

/* feature tiles */
.tile{position:absolute;width:156px;height:86px;border:1px solid var(--tile-border);background:linear-gradient(#fff 60%,#f6f6f6);box-shadow:0 1px 2px rgba(0,0,0,.08);text-align:center}
.tile svg{position:absolute;left:63px;top:18px}
.tile-label{position:absolute;left:0;right:0;top:53px;font-family:"Raleway",sans-serif;font-size:12.5px;color:var(--brand)}

/* intro band */
.intro-band{position:absolute;left:0;top:633px;width:796px;height:80px;background:linear-gradient(#f7f7f7,#ececec);border-top:1px solid #e2e2e2;border-bottom:1px solid #e2e2e2;text-align:center;font-family:"Raleway",sans-serif}
.intro-title{margin-top:24px;font-size:14.5px;color:#333}
.intro-sub{margin-top:3px;font-size:10.5px;color:#777}

/* community */
.section-title{position:absolute;left:0;width:796px;top:756px;text-align:center;font-family:"Raleway",sans-serif;font-size:18.5px;color:#333}
.activity{position:absolute;width:270px}
.avatar{position:absolute;left:0;top:2px;width:26px;height:26px}
.avatar.brand-square{background:var(--brand);color:#fff;font-size:5.5px;display:flex;align-items:center;justify-content:center}
.avatar.photo{background:linear-gradient(#cbbca9,#8d7a68)}
.activity-body{position:absolute;left:35px;top:0;width:240px}
.activity-title{font-size:7px;color:#444;line-height:10px}
.activity-note{font-size:5.8px;color:#555;line-height:10px}
.activity-time{font-size:5.8px;color:var(--brand);line-height:10px}

/* footer */
.site-footer{position:absolute;left:0;top:1010px;width:796px;height:152px;background:linear-gradient(#0b86d0,#0062b8)}
.footer-col{position:absolute;top:32px}
.footer-col h4{font-family:"Raleway",sans-serif;font-size:10.5px;font-weight:500;color:#fff;margin-bottom:5px}
.footer-col li{list-style:none;font-size:7.5px;color:#e6f1fb;line-height:12.8px}
.footer-divider{position:absolute;top:32px;width:1px;height:85px;background:rgba(255,255,255,.3)}
.social-dot{display:inline-block;width:13px;height:13px;border-radius:50%;background:#fff;margin-right:7px}
.footer-bottom{position:absolute;left:0;top:1162px;width:796px;height:38px;background:#0058a8}
.copyright{position:absolute;left:126px;top:14px;font-size:6.5px;color:#bcd6ef}
</style>
</head>
<body>

<header class="site-header">
  <div class="abs brand-name">Vetrola</div>
  <div class="abs brand-tagline">Connecting People to Online Learning</div>
  <nav class="main-nav">
    <a style="left:313px">Forums</a>
    <a style="left:373px">Resources</a>
    <a style="left:446px">Members</a>
    <a style="left:514px">Blog</a>
  </nav>
  <div class="btn-outline" style="left:560px;width:55px">Sign Up</div>
  <div class="btn-outline" style="left:622px;width:55px">Log In</div>
</header>

<section class="hero" role="img" aria-label="Photo of a smiling student lying on a bed using a laptop">
  <div class="hero-title line1">At the heart of connecting people to</div>
  <div class="hero-title line2">Online learning</div>
  <div class="hero-cta">Sign Up for Free</div>
  <svg class="hero-arrow" style="left:78px" width="26" height="58" viewBox="0 0 26 58"><path d="M24 1 L2 29 L24 57" fill="none" stroke="#777" stroke-width="1.2"/></svg>
  <svg class="hero-arrow" style="left:694px" width="26" height="58" viewBox="0 0 26 58"><path d="M2 1 L24 29 L2 57" fill="none" stroke="#777" stroke-width="1.2"/></svg>
</section>

<section class="features">
  <div class="tile" style="left:152px;top:420px">
    <svg width="28" height="28" viewBox="0 0 28 28"><circle cx="14" cy="14" r="12" fill="var(--brand)"/><path d="M8 14.5 L12.5 19 L20 10" fill="none" stroke="#fff" stroke-width="3"/></svg>
    <div class="tile-label">Getting Started</div>
  </div>
  <div class="tile" style="left:323px;top:420px">
    <svg width="30" height="28" viewBox="0 0 30 28"><path d="M3 11 C3 6 8 3 13 3 C18 3 23 6 23 11 C23 16 18 19 13 19 L7 23 L8 18 C5 17 3 14 3 11Z" fill="none" stroke="var(--brand)" stroke-width="2.3"/><path d="M25 11 C27 12.5 28 14 28 16 C28 18.5 26.5 20 25 21 L26 25 L21 22 C18 22 16 21 14.5 20" fill="none" stroke="var(--brand)" stroke-width="2.3"/></svg>
    <div class="tile-label">Discussions</div>
  </div>
  <div class="tile" style="left:494px;top:420px">
    <svg width="28" height="28" viewBox="0 0 28 28"><path d="M5 19 L18 6 L22 10 L9 23 L4 24Z" fill="var(--brand)"/><path d="M19.5 4.5 L21.5 2.5 L25.5 6.5 L23.5 8.5Z" fill="var(--brand)"/></svg>
    <div class="tile-label">Reviews</div>
  </div>
  <div class="tile" style="left:152px;top:518px">
    <svg width="28" height="28" viewBox="0 0 28 28"><path d="M5 1 H17 L24 8 V27 H5Z" fill="var(--brand)"/><path d="M17 1 V8 H24" fill="#fff" opacity=".5"/><path d="M9 14 H20 M9 18 H20 M9 22 H20" stroke="#fff" stroke-width="1.6"/></svg>
    <div class="tile-label">Tips &amp; Guidelines</div>
  </div>
  <div class="tile" style="left:323px;top:518px">
    <svg width="28" height="28" viewBox="0 0 28 28"><rect x="2" y="4" width="24" height="22" rx="1.5" fill="var(--brand)"/><rect x="8" y="1" width="3" height="6" fill="var(--brand)"/><rect x="17" y="1" width="3" height="6" fill="var(--brand)"/><path d="M5 10 H23 V23 H5Z M5 14.3 H23 M5 18.6 H23 M9.5 10 V23 M14 10 V23 M18.5 10 V23" fill="none" stroke="#fff" stroke-width="1"/></svg>
    <div class="tile-label">News &amp; Articles</div>
  </div>
  <div class="tile" style="left:494px;top:518px">
    <svg width="28" height="28" viewBox="0 0 28 28"><rect x="1" y="5" width="26" height="19" rx="2" fill="var(--brand)"/><path d="M2 7 L14 16 L26 7" fill="none" stroke="#fff" stroke-width="1.8"/></svg>
    <div class="tile-label">Newsletter</div>
  </div>
</section>

<section class="intro-band">
  <div class="intro-title">Mauris vel lacus vitae felis vestibulum</div>
  <div class="intro-sub">Etiam est nunc venenatis in tristique eu imperdiet ac nisl Cum&nbsp; Etiam eu urna Sed porta</div>
</section>

<h2 class="section-title" style="font-weight:400">From the Community</h2>

<section class="community">
  <div class="activity" style="left:117px;top:812px">
    <div class="avatar brand-square">Vetrola</div>
    <div class="activity-body">
      <div class="activity-title">Carolyn posted the resource Guide How to select the right MOOC.</div>
      <div class="activity-note">A step-by-step approach to finding the right MOOC for you</div>
      <div class="activity-time">Monday at 4:02 PM</div>
    </div>
  </div>
  <div class="activity" style="left:117px;top:867px">
    <div class="avatar brand-square">Vetrola</div>
    <div class="activity-body">
      <div class="activity-title">Carolyn posted a new thread.</div>
      <div class="activity-note">What Reviews divulge about Online Education</div>
      <div class="activity-time">Monday at 4:02 PM</div>
    </div>
  </div>
  <div class="activity" style="left:117px;top:922px">
    <div class="avatar brand-square">Vetrola</div>
    <div class="activity-body">
      <div class="activity-title">Carolyn liked Tom's post in the thread Advice How do you "unenroll" from a course on Learnova?.</div>
      <div class="activity-note">Thanks for this Carolyn, very handy when you've over-subscribed to free courses</div>
      <div class="activity-time">Monday at 4:02 PM</div>
    </div>
  </div>
  <div class="activity" style="left:411px;top:812px">
    <div class="avatar photo" role="img" aria-label="Member profile photo"></div>
    <div class="activity-body">
      <div class="activity-title">Tom replied to the thread Advice How do you "unenroll" from a course on Learnova?.</div>
      <div class="activity-note">Thanks for this Carolyn, very handy when you've over-subscribed to free courses</div>
      <div class="activity-time">Monday at 4:02 PM</div>
    </div>
  </div>
  <div class="activity" style="left:411px;top:866px">
    <div class="avatar photo" role="img" aria-label="Member profile photo"></div>
    <div class="activity-body">
      <div class="activity-title">Tom set their occupation to Digital marketing consultant.</div>
      <div class="activity-note">What Reviews divulge about Online Education</div>
      <div class="activity-time">Monday at 4:02 PM</div>
    </div>
  </div>
  <div class="activity" style="left:411px;top:921px">
    <div class="avatar brand-square">Vetrola</div>
    <div class="activity-body">
      <div class="activity-title">Carolyn posted the resource Infographic MOOCs Pros &amp; Cons.</div>
      <div class="activity-note">Thanks for this Carolyn, very handy when you've over-subscribed to free courses</div>
      <div class="activity-time">Monday at 4:02 PM</div>
    </div>
  </div>
</section>

<footer class="site-footer">
  <div class="footer-col" style="left:131px"><h4>COMPANY</h4><ul><li>Home</li><li>Recent Activity</li><li>What's New?</li><li>Help</li><li>Forums</li></ul></div>
  <div class="footer-divider" style="left:217px"></div>
  <div class="footer-col" style="left:250px"><h4>RESOURCES</h4><ul><li>Resources</li><li>Members</li><li>FAQ</li><li>Blog</li><li>Vetrola</li></ul></div>
  <div class="footer-divider" style="left:335px"></div>
  <div class="footer-col" style="left:366px"><h4>SUPPORT</h4><ul><li>Chirply Feed</li><li>Recent Activities</li><li>New Threads</li><li>Community Guidlines</li></ul></div>
  <div class="footer-divider" style="left:468px"></div>
  <div class="footer-col" style="left:506px"><h4>FOLLOW US</h4><ul><li>Please connect with us on</li></ul>
    <div style="margin-top:8px"><span class="social-dot"></span><span class="social-dot"></span><span class="social-dot"></span><span class="social-dot"></span></div>
  </div>
</footer>
<div class="footer-bottom"><div class="copyright">© 2015 Company Name&nbsp; All right reserved&nbsp; Term of Use</div></div>

</body>
</html>
```